Business Card Design for Kind Helper

I am starting my own consultancy business, using what I learned in marketing and advertising to help Non -profits with marketing and communications needs. I need a professional business card design to hand out to my clients.

My business name is “Outreach2Kindness” my vision is that this need this to be reflective of marketing doing good for the world through the power of communications. I like the color palettes in olives, creams and oranges but am open to design options.
In addition to the cards I am asking for separate file for the logo and will need a JPG, PSD Vector File.

Information to go on the card:

Morwenna Calloway
Marketing Consultant
Email: outreach2kindness@mailbrook.com, callowaym1@brinmoreu.edu
Website: Outreach2Kindness.com

Communications

```html
<!DOCTYPE html>
<html lang="en">
<head>
<meta charset="utf-8">
<title>Outreach2Kindness — Business Card</title>
<link rel="stylesheet" href="https://fonts.googleapis.com/css2?family=EB+Garamond:wght@700;800&display=swap">
<style>
  :root {
    --page: #ffffff;
    --olive: #bdbf4c;
    --leaf: #dfe34a;
    --leaf-soft: rgba(223, 227, 74, 0.55);
    --cream: #f4e27f;
    --glow-core: #fff200;
    --glow-edge: #fffbdc;
    --orange: #f39200;
    --orange-soft: #f6aa3a;
    --mark: #d9dc3e;
    --ink: #2f2a25;
  }
  * { margin: 0; padding: 0; box-sizing: border-box; }
  html, body { width: 1200px; height: 1000px; overflow: hidden; background: var(--page); }
  body { position: relative; font-family: "EB Garamond", Garamond, "Times New Roman", serif; color: var(--ink); }

  .card { position: absolute; width: 504px; height: 288px; overflow: hidden; background: var(--olive); }
  .card svg.card-art { position: absolute; inset: 0; width: 100%; height: 100%; }
  .card-front { left: 124px; top: 175px; }
  .card-back { left: 592px; top: 564px; }

  /* soft placeholders for the scattered leaf decoration */
  .leaf-scatter { position: absolute; }
  .card-front .leaf-scatter {
    inset: 0;
    background:
      radial-gradient(ellipse 60px 40px at 75px 45px, var(--leaf-soft), transparent 70%),
      radial-gradient(ellipse 60px 40px at 440px 40px, var(--leaf-soft), transparent 70%),
      radial-gradient(ellipse 50px 35px at 330px 55px, var(--leaf-soft), transparent 70%),
      radial-gradient(ellipse 50px 35px at 36px 142px, var(--leaf-soft), transparent 70%),
      radial-gradient(ellipse 50px 35px at 440px 138px, var(--leaf-soft), transparent 70%),
      radial-gradient(ellipse 60px 40px at 52px 245px, var(--leaf-soft), transparent 70%),
      radial-gradient(ellipse 60px 40px at 438px 245px, var(--leaf-soft), transparent 70%);
  }
  .card-back .leaf-scatter {
    left: 0; top: 0; width: 504px; height: 288px;
    background:
      radial-gradient(ellipse 170px 110px at 390px 110px, var(--leaf-soft), transparent 72%),
      radial-gradient(ellipse 90px 60px at 140px 225px, var(--leaf-soft), transparent 72%),
      radial-gradient(ellipse 40px 30px at 34px 240px, var(--leaf-soft), transparent 72%);
  }

  .brand-mark { position: absolute; border-radius: 50%; background: var(--mark); }
  .brand-name { position: absolute; font-weight: 800; color: var(--ink); white-space: nowrap; }

  .card-front .brand-mark { left: 216px; top: 62px; width: 72px; height: 72px; }
  .card-front .brand-name { left: 0; width: 100%; top: 140px; text-align: center; font-size: 28px; line-height: 34px; }
  .card-front .web { position: absolute; left: 0; width: 100%; top: 208px; text-align: center; font-size: 17px; font-weight: 800; }

  .card-back .brand-mark { left: 96px; top: 22px; width: 56px; height: 56px; }
  .card-back .brand-name { left: 24px; top: 84px; font-size: 19px; line-height: 22px; }
  .holder-name { position: absolute; left: 22px; top: 132px; font-size: 25px; font-weight: 800; line-height: 30px; }
  .holder-role { position: absolute; left: 22px; top: 169px; font-size: 17px; font-weight: 800; line-height: 20px; }
  .contact { position: absolute; left: 232px; top: 213px; font-size: 13.5px; font-weight: 800; line-height: 18px; white-space: nowrap; }
  .contact .indent { padding-left: 44px; display: block; }
</style>
</head>
<body>

<section class="card card-front" aria-label="Card front">
  <div class="leaf-scatter" role="img" aria-label="Scattered light green leaf decoration"></div>
  <svg class="card-art" viewBox="0 0 504 288" aria-hidden="true">
    <defs>
      <radialGradient id="glow" cx="0.5" cy="0.5" r="0.5">
        <stop offset="0" stop-color="var(--glow-core)"/>
        <stop offset="0.35" stop-color="var(--glow-core)" stop-opacity="0.85"/>
        <stop offset="1" stop-color="var(--glow-edge)"/>
      </radialGradient>
    </defs>
    <ellipse cx="252" cy="159" rx="178" ry="100" fill="url(#glow)"/>
  </svg>
  <div class="brand-mark" aria-hidden="true"></div>
  <div class="brand-name">Outreach2Kindness</div>
  <div class="web">Outreach2Kindness.com</div>
</section>

<section class="card card-back" aria-label="Card back">
  <svg class="card-art" viewBox="0 0 504 288" aria-hidden="true">
    <path d="M0,276 Q290,168 468,0 L504,0 L504,288 L0,288 Z" fill="var(--cream)"/>
    <path d="M184,288 Q370,150 492,0 L504,0 L504,288 Z" fill="var(--orange)"/>
    <path d="M312,288 L504,36 L504,288 Z" fill="var(--orange-soft)"/>
  </svg>
  <div class="leaf-scatter" role="img" aria-label="Scattered light green leaf decoration"></div>
  <div class="brand-mark" aria-hidden="true"></div>
  <div class="brand-name">Outreach2Kindness</div>
  <div class="holder-name">Morwenna Calloway</div>
  <div class="holder-role">Marketing Consultant</div>
  <div class="contact">
    Email: outreach2kindness@mailbrook.com
    <span class="indent">callowaym1@brinmoreu.edu</span>
    Website: Outreach2Kindness.com
  </div>
</section>

</body>
</html>
```